Label to go onto food packaging.

We need to create a visually interesting and appealing label to stick onto our take away food packaging. The label should contain information of the food products our cafe sells. The label is to go onto biodegradable food bowls and clam shell packaging.
The information is basically the lines we sell - buddha bowls, super smoothies, vegan burgers and curries. And also the slogan 'nourish and refresh'. We have a logo design that we would like to incorporate onto the label (but not essential)
The design will go onto a rectangle strip label.
The colours of our food outlet are splashes of yellow, blue and grey in a white interior.
We also feature a large garden green wall. You may view images from our instagram page quiet pebble kitchen

Target Market(s)

Young professional, health conscious, plant based eaters. To be used on takeaway packaging.

Industry/Entity Type

Food Production

Font styles to use
Sans Serif

Colors

Designer to choose colors to be used in the design.

Requirements
Must have
• Bold, appealing, informative.
Nice to have
• Logo incorporated, possibly as a watermark?
Should not have
• No floral shapes. If incorporating the logo, use a circle or nothing around it. No pictures/photos of food

```html
<!DOCTYPE html>
<html lang="en">
<head>
<meta charset="utf-8">
<title>Quiet Pebble Kitchen – Takeaway Labels</title>
<link rel="stylesheet" href="https://fonts.googleapis.com/css2?family=Montserrat:wght@700&family=Kanit:wght@800&family=Kaushan+Script&display=swap">
<style>
  :root {
    --leaf: #8cc63f;
    --ink: #231f20;
    --paper: #ffffff;
  }
  html, body {
    margin: 0;
    padding: 0;
    overflow: hidden;
    background: var(--paper);
  }
  .canvas {
    position: relative;
    width: 1200px;
    height: 1000px;
    background: var(--paper);
    overflow: hidden;
  }
  .label {
    position: absolute;
    left: 200px;
    width: 840px;
    height: 232px;
  }
  .label--menu { top: 220px; }
  .label--range { top: 547px; }
  .label__art {
    position: absolute;
    inset: 0;
  }
  .brand {
    position: absolute;
    left: 18px;
    top: 46px;
    width: 134px;
    height: 134px;
    border: 4px solid var(--ink);
    border-radius: 50%;
    box-sizing: border-box;
    display: flex;
    flex-direction: column;
    align-items: center;
    justify-content: center;
    font-family: "Montserrat", sans-serif;
    font-weight: 700;
    color: var(--ink);
    font-size: 15px;
    line-height: 1.1;
    text-align: center;
    letter-spacing: 0.5px;
  }
  .slogan {
    position: absolute;
    left: 210px;
    width: 620px;
    text-align: center;
    font-family: "Montserrat", sans-serif;
    font-weight: 700;
    color: var(--ink);
    margin: 0;
  }
  .label--menu .slogan { top: 44px; font-size: 26px; letter-spacing: 0.5px; }
  .label--range .slogan { top: 18px; font-size: 20px; letter-spacing: 0.5px; }
  .dish {
    position: absolute;
    left: 210px;
    width: 620px;
    top: 68px;
    margin: 0;
    text-align: center;
    font-family: "Kanit", sans-serif;
    font-weight: 800;
    font-size: 76px;
    line-height: 1.2;
    color: var(--ink);
    letter-spacing: 0.5px;
  }
  .ingredients {
    position: absolute;
    left: 210px;
    width: 620px;
    top: 164px;
    margin: 0;
    text-align: center;
    font-family: "Kaushan Script", cursive;
    font-size: 19px;
    color: var(--ink);
  }
  .range {
    position: absolute;
    left: 240px;
    width: 560px;
    top: 82px;
    margin: 0;
    text-align: center;
    font-family: "Kanit", sans-serif;
    font-weight: 800;
    font-size: 36px;
    line-height: 41px;
    color: var(--leaf);
    text-transform: uppercase;
    transform: rotate(-4.5deg);
    transform-origin: center;
  }
</style>
</head>
<body>
<div class="canvas">

  <section class="label label--menu">
    <svg class="label__art" width="840" height="232" viewBox="0 0 840 232" aria-hidden="true">
      <rect x="160" y="1" width="672" height="231" fill="var(--leaf)"/>
      <path fill="var(--ink)" d="M160,1 C195,1 206,20 206,52 L206,98 C206,110 212,117 224,117 C212,117 206,124 206,136 L206,190 C206,218 195,232 160,232 Z"/>
      <path fill="var(--paper)" d="M160,1 C180,1 186,20 186,52 L186,98 C186,110 192,117 200,117 C192,117 186,124 186,136 L186,190 C186,218 180,232 160,232 Z"/>
    </svg>
    <div class="brand"><span>QUIET</span><span>PEBBLE</span><span>KITCHEN</span></div>
    <p class="slogan">NOURISH &amp; REFRESH</p>
    <h2 class="dish">Vegan Burger</h2>
    <p class="ingredients">Green onions, Cumin, Mushrooms, Pinto beans, Parsley</p>
  </section>

  <section class="label label--range">
    <svg class="label__art" width="840" height="232" viewBox="0 0 840 232" aria-hidden="true">
      <rect x="160" y="1" width="672" height="231" fill="var(--leaf)"/>
      <path fill="var(--paper)" d="M160,1 C182,1 192,20 192,52 L192,104 C192,112 186,116 180,116 C186,116 192,120 192,130 L192,190 C192,218 182,232 160,232 Z"/>
      <polygon fill="var(--ink)" points="240,86 760,32 782,232 254,232"/>
      <g fill="var(--leaf)">
        <circle cx="248" cy="85" r="4"/><circle cx="268" cy="83" r="4"/><circle cx="288" cy="81" r="4"/>
        <circle cx="308" cy="79" r="4"/><circle cx="328" cy="77" r="4"/><circle cx="348" cy="75" r="4"/>
        <circle cx="368" cy="73" r="4"/><circle cx="388" cy="71" r="4"/><circle cx="408" cy="68" r="4"/>
        <circle cx="428" cy="66" r="4"/><circle cx="448" cy="64" r="4"/><circle cx="468" cy="62" r="4"/>
        <circle cx="488" cy="60" r="4"/><circle cx="508" cy="58" r="4"/><circle cx="528" cy="56" r="4"/>
        <circle cx="548" cy="54" r="4"/><circle cx="568" cy="52" r="4"/><circle cx="588" cy="50" r="4"/>
        <circle cx="608" cy="48" r="4"/><circle cx="628" cy="46" r="4"/><circle cx="648" cy="44" r="4"/>
        <circle cx="668" cy="42" r="4"/><circle cx="688" cy="39" r="4"/><circle cx="708" cy="37" r="4"/>
        <circle cx="728" cy="35" r="4"/><circle cx="748" cy="33" r="4"/>
      </g>
    </svg>
    <div class="brand"><span>QUIET</span><span>PEBBLE</span><span>KITCHEN</span></div>
    <p class="slogan">NOURISH &amp; REFRESH</p>
    <p class="range">Buddha bowls,<br>super smoothies, curries<br>and vegan burgers</p>
  </section>

</div>
</body>
</html>
```